Stationery Design Project for Explainer Video Company

We are a company for explainer videos. We are working together with a community consisting of creative people. The vorbilo videos are animated. Please visit our homepage at www.vorbilo-studio.de, we like our Monitor-Logo, so please create a similar stationary to that. you might use the colours and the font (Pacifico or similar)
We need business cards too. We don't need Facsimile
attached is the logo (please don't use chatterbox text)

Target Market(s)

Marketing, SMB

Industry/Entity Type

Business

```html
<!DOCTYPE html>
<html lang="de">
<head>
<meta charset="utf-8">
<title>vorbilo – Geschäftsausstattung</title>
<link rel="stylesheet" href="https://fonts.googleapis.com/css2?family=Open+Sans:wght@400;600;700&family=Pacifico&family=Allura&display=swap">
<style>
  :root {
    --blue: #1a9cc7;
    --blue-deep: #0e80b9;
    --red: #d8262e;
    --paper: #ffffff;
    --ink: #55585c;
    --ink-dark: #2f3135;
    --window: #ececec;
    --backdrop: #e9eaeb;
  }
  * { box-sizing: border-box; margin: 0; padding: 0; }
  html, body { width: 1200px; height: 801px; overflow: hidden; }
  body {
    background: var(--backdrop);
    font-family: "Open Sans", Arial, sans-serif;
    color: var(--ink);
    position: relative;
  }
  .sheet {
    position: absolute;
    background: var(--paper);
    overflow: hidden;
    box-shadow: 0 2px 10px rgba(0,0,0,.12);
  }
  .brand { display: flex; align-items: center; gap: 10px; }
  .brand-dot { border-radius: 50%; background: var(--red); flex: none; }
  .brand-name {
    font-family: "Pacifico", cursive;
    font-weight: 400;
    color: var(--blue);
    line-height: 1.3;
  }
  .footer-band {
    position: absolute; left: 0; bottom: 0;
    background: linear-gradient(180deg, var(--blue), var(--blue-deep));
  }

  /* Letterhead */
  .letterhead { left: 50px; top: 50px; width: 495px; height: 700px; }
  .letterhead .brand { position: absolute; left: 40px; top: 40px; }
  .letterhead .brand-dot { width: 44px; height: 44px; }
  .letterhead .brand-name { font-size: 30px; }
  .letter-body { position: absolute; left: 40px; top: 128px; width: 405px; font-size: 9.5px; line-height: 1.55; }
  .letter-greeting { font-weight: 700; color: var(--ink-dark); margin-bottom: 12px; font-size: 10px; }
  .letter-body p { margin-bottom: 10px; }
  .signature { position: absolute; left: 40px; top: 430px; }
  .signature-name { font-family: "Allura", cursive; font-size: 40px; color: var(--ink-dark); line-height: 1.1; }
  .signature-role { font-weight: 700; font-size: 10px; color: var(--ink); margin-top: 2px; }
  .letterhead .footer-band { width: 100%; height: 140px; }
  .letter-contact {
    position: absolute; left: 40px; bottom: 32px;
    color: #fff; font-size: 10.5px; line-height: 1.6; font-style: normal;
  }

  /* Envelope */
  .envelope { left: 610px; top: 60px; width: 540px; height: 270px; }
  .envelope .brand { position: absolute; left: 34px; top: 96px; }
  .envelope .brand-dot { width: 30px; height: 30px; }
  .envelope .brand-name { font-size: 22px; }
  .envelope-window {
    position: absolute; right: 34px; top: 36px; width: 160px; height: 74px;
    border-radius: 9px; background: var(--window);
    box-shadow: inset 0 0 0 1px #dedede;
  }
  .envelope .footer-band { width: 310px; height: 62px; }
  .envelope-address {
    position: absolute; left: 34px; bottom: 16px;
    color: #fff; font-size: 8px; line-height: 1.5; font-style: normal;
  }

  /* Business card */
  .business-card {
    left: 610px; top: 380px; width: 380px; height: 246px;
    background: linear-gradient(135deg, var(--blue-deep), var(--blue) 70%);
  }
  .card-corner { position: absolute; background: #fff; }
  .card-corner.top { right: 0; top: 0; width: 70px; height: 100px; }
  .card-corner.bottom { left: 0; bottom: 0; width: 150px; height: 44px; }
  .business-card .brand { position: absolute; left: 0; right: 0; top: 92px; justify-content: center; }
  .business-card .brand-dot { width: 40px; height: 40px; }
  .business-card .brand-name { color: #fff; font-size: 34px; }
</style>
</head>
<body>

  <article class="sheet letterhead">
    <div class="brand">
      <span class="brand-dot"></span>
      <span class="brand-name">vorbilo</span>
    </div>

    <div class="letter-body">
      <p class="letter-greeting">Lorem Ipsum,</p>
      <p>Cras mattis consectetur purus sit amet fermentum. Etiam porta sem malesuada magna mollis euismod. Aenean lacinia bibendum nulla sed consectetur.</p>
      <p>Vivamus sagittis lacus vel augue laoreet rutrum faucibus dolor auctor. Nullam quis risus eget urna mollis ornare vel eu leo.</p>
      <p>Donec id elit non mi porta gravida at eget metus. Maecenas faucibus mollis interdum.</p>
      <p>Cum sociis natoque penatibus et magnis dis parturient montes, nascetur ridiculus mus.</p>
      <p>Cras mattis consectetur purus sit amet, vestibulum at eros. Donec odio sem nec elit. Integer posuere erat a ante venenatis dapibus posuere velit aliquet. Vivamus sagittis lacus vel augue laoreet rutrum faucibus dolor auctor.</p>
    </div>

    <div class="signature">
      <div class="signature-name">Your Name</div>
      <div class="signature-role">Company Director</div>
    </div>

    <div class="footer-band" role="img" aria-label="Blue cloud illustration along the bottom edge"></div>
    <address class="letter-contact">
      +49 (8031) 47 22 16<br>
      anna.keller@vorbilo.de<br>
      Lindwerk GmbH &amp; Co KG<br>
      Ahornweg 14, 83022 Rosenheim, Deutschland
    </address>
  </article>

  <article class="sheet envelope">
    <div class="brand">
      <span class="brand-dot"></span>
      <span class="brand-name">vorbilo</span>
    </div>
    <div class="envelope-window"></div>
    <div class="footer-band" role="img" aria-label="Blue cloud illustration in the lower left corner"></div>
    <address class="envelope-address">
      Lindwerk GmbH &amp; Co KG<br>
      Ahornweg 14, 83022 Rosenheim, Deutschland
    </address>
  </article>

  <article class="sheet business-card">
    <div class="card-corner top" role="img" aria-label="White cloud illustration in the upper right corner"></div>
    <div class="card-corner bottom" role="img" aria-label="White cloud illustration in the lower left corner"></div>
    <div class="brand">
      <span class="brand-dot"></span>
      <span class="brand-name">vorbilo</span>
    </div>
  </article>

</body>
</html>
```